New Business Card Design for Business Consulting Business

We need a business card design that reflects the simplicity of our business. We partner with our clients to help them deliver change. We are a different kind of business consulting group. We don't just provide you with the theory. We provide you with the leadership and capability to execute change.

Vonduro is a professional services organisation that partners with their clients to lead the execution of strategic process and system improvement initiatives. Vonduro combines hands on delivery with coaching in best practice methodologies and approaches to build their clients capabilities to ensure their ongoing success in project implementations. Vonduro offers business advisory services in Project Management, Business Process Management, Change Management and Business Analytics.

Reason: Hi Designers, Thanks for all of your great designs. There are some really creative and cool ideas. Everyone is really capturing the essence of my business Vonduro. I am extending the deadline for the business card design by 6 days as I need to consult my Marketing colleague who won't be back in Australia until Wednesday. I would like to sit down with them and review all of the best designs. The key themes of the things I have really liked on my first review are: 1) Capturing the company website on the back of the card. 2) Including the company logo on the back of the card too. 3) Including the types of services on the back of the card that the company offers - Project Management - Business Process Management - Change Management - Business Analytics 4) Utilising some images on the back of the card Just so everyone knows the colour palette for the Vonduro company logo is: R: 0 G: 86 B: 162 or C: 97% M: 73% Y: 4% K: 0% Thanks Gareth

Hi Designers,

Thanks for all of your submissions to date.  I am working through each design and will provide feedback on all the great work.

One thing I would like to ask is if you could submit a version that has my academic credentials under or after my name.  I am not a big fan of doing this but as I am in business consulting it does seem to be quite common.

I hold a Bachelor of Commerce (BCom) and a Master of Business Administration (MBA)

Thanks

Gareth

Hi Designers,

Thanks for all of your fantastic designs.  There are some really great designs here for my business.  I am still in the process of reviewing designs and should have this completed by tomorrow.  Some of the things I have learnt from this round of designs are:

1) I prefer to have the card without my academic qualifications

2) I really like cards that have a blue back

3) I prefer to have my name and title either left or right of centre

I hope this helps and I will endeavour to get through all of the designs tomorrow

Cheers

Gareth

Target Market(s)

We target large corporate organisations

Industry/Entity Type

Leadership

Requirements
Must have
• Must have the following business details

Gareth Pilling - Director
Address: Level 7, 82 Harlow Street, Melbourne, Australia, 3000
Phone: +61 3 527 840 213
Fax: +61 3 9214 5037
Email: gareth.pilling@vonduro-example.com.au
LinkedIn: au.linkedin.com/in/garethjpilling/
Twiiter: @garethjpilling
Website: www.vonduro-example.com.au

```html
<!DOCTYPE html>
<html lang="en">
<head>
<meta charset="utf-8">
<title>Vonduro business card</title>
<link rel="stylesheet" href="https://fonts.googleapis.com/css2?family=Abel&display=swap">
<style>
  :root {
    --brand-blue: #0056a2;
    --paper: #ffffff;
    --ink: #111111;
    --backdrop: #e9e6e1;
  }
  * { box-sizing: border-box; margin: 0; padding: 0; }
  html, body {
    width: 1200px;
    height: 900px;
    overflow: hidden;
    background: var(--backdrop);
    font-family: "Abel", sans-serif;
  }
  .card-set {
    position: relative;
    width: 1200px;
    height: 900px;
  }
  .card {
    position: absolute;
    top: 106px;
    width: 420px;
    height: 688px;
    box-shadow: 0 8px 24px rgba(0,0,0,0.18);
  }
  .card--back {
    left: 150px;
    background: var(--brand-blue);
    color: var(--paper);
  }
  .card--front {
    left: 630px;
    background: var(--paper);
    color: var(--ink);
  }

  .wordmark {
    position: absolute;
    left: 0;
    right: 0;
    display: flex;
    align-items: center;
    justify-content: center;
    gap: 12px;
    font-size: 76px;
    line-height: 1;
    letter-spacing: 1px;
  }
  .wordmark__dot {
    width: 26px;
    height: 26px;
    border-radius: 50%;
    background: currentColor;
    flex: none;
  }
  .card--back .wordmark { top: 210px; }
  .card--front .wordmark { top: 118px; color: var(--brand-blue); }

  .tab {
    position: absolute;
    height: 40px;
    width: 132px;
    background: var(--brand-blue);
  }
  .tab--top { top: 0; left: 130px; }
  .tab--bottom { bottom: 0; left: 200px; }

  .holder {
    position: absolute;
    top: 292px;
    left: 0;
    right: 0;
    text-align: center;
  }
  .holder__name {
    font-size: 46px;
    font-weight: 400;
    color: var(--brand-blue);
    line-height: 1.05;
  }
  .holder__title {
    font-size: 28px;
    color: var(--ink);
    margin-top: 2px;
    padding-left: 110px;
  }

  .contact {
    position: absolute;
    left: 30px;
    right: 20px;
    top: 448px;
    display: grid;
    grid-template-columns: 86px 1fr;
    row-gap: 3px;
    font-size: 17px;
    line-height: 1.2;
  }
  .contact dt { color: var(--brand-blue); }
  .contact dd { color: var(--ink); white-space: nowrap; }
</style>
</head>
<body>
<main class="card-set">
  <section class="card card--back" aria-label="Card back">
    <div class="wordmark"><span>Vonduro</span><span class="wordmark__dot"></span></div>
  </section>

  <section class="card card--front" aria-label="Card front">
    <div class="tab tab--top"></div>
    <div class="wordmark"><span>Vonduro</span><span class="wordmark__dot"></span></div>

    <div class="holder">
      <h1 class="holder__name">Gareth Pilling</h1>
      <p class="holder__title">Director</p>
    </div>

    <dl class="contact">
      <dt>Address:</dt><dd>Level 7, 82 Harlow Street,<br>Melbourne, Australia, 3000</dd>
      <dt>Phone:</dt><dd>+61 3 527 840 213</dd>
      <dt>Fax:</dt><dd>+61 3 9214 5037</dd>
      <dt>Email:</dt><dd>gareth.pilling@vonduro-example.com.au</dd>
      <dt>Twitter:</dt><dd>@garethjpilling</dd>
      <dt>LinkedIn:</dt><dd>au.linkedin.com/in/garethjpilling/</dd>
      <dt>Website:</dt><dd>www.vonduro-example.com.au</dd>
    </dl>

    <div class="tab tab--bottom"></div>
  </section>
</main>
</body>
</html>
```